Concise,Good colour matching,Good looks design for "HERD SURE QUICK ASSAY FOR LIVESTOCK"

Product Positioning: Affordable test for Large Animals (Livestock/Veterinary Use)
Product Name: HERD SURE Quick Assay Kit (for large animals, e.g., cattle, horses, swine,Avian,sheep).

2. Packaging Requirements

A. Visual Design
Color Scheme:
Green/Blue/Orange/Yellow/Red/Gray/White(chose 2~4 colors)

Mandatory Info:
Brand logo ("HERD SURE")

Target Market(s)

Southeast Asia, Africa, Middle East, South America

Industry/Entity Type

Veterinary diagnostic for LIVESTOCK

Colors

Designer to choose colors to be used in the design.

Requirements
Nice to have
• Concise,Good colour matching,Good looks

```html
<!DOCTYPE html>
<html lang="en">
<head>
<meta charset="utf-8">
<title>HERD SURE Quick Assay Kit – Packaging Panels</title>
<link href="https://fonts.googleapis.com/css2?family=Poppins:wght@400;500;600;700;800&display=swap" rel="stylesheet">
<style>
  :root {
    --bg: #858585;
    --teal: #00a99d;
    --teal-dark: #0a9a8f;
    --slate: #bfcbd3;
    --slate-dark: #a9b7c1;
    --photo: #7d8890;
    --white: #ffffff;
    --ink: #111111;
  }
  * { margin: 0; padding: 0; box-sizing: border-box; }
  html, body { width: 1200px; height: 3333px; overflow: hidden; }
  body {
    background: var(--bg);
    font-family: "Poppins", sans-serif;
    position: relative;
  }
  .panel { position: absolute; overflow: hidden; }
  .wordmark {
    font-weight: 800;
    letter-spacing: -2px;
    line-height: 1;
    white-space: nowrap;
  }
  .tagline { font-weight: 500; white-space: nowrap; }

  /* header brand */
  .brand-header {
    position: absolute; left: 65px; top: 68px;
    color: var(--white); font-size: 84px;
  }

  /* front panel */
  .front { left: 226px; top: 854px; width: 747px; height: 397px; background: var(--teal); }
  .front .pattern { position: absolute; inset: 0; background: linear-gradient(160deg, #15b3a7 0%, var(--teal) 50%, #0ca196 100%); }
  .front .wordmark { position: absolute; left: 0; right: 0; top: 185px; text-align: center; color: var(--white); font-size: 58px; }
  .front .tagline { position: absolute; left: 0; right: 0; top: 253px; text-align: center; color: var(--white); font-size: 23px; }

  /* top panel with animal photos */
  .top { left: 225px; top: 1285px; width: 750px; height: 549px; background: var(--white); }
  .photo-grid { position: absolute; left: 0; top: 0; width: 750px; height: 374px; display: grid; grid-template-columns: repeat(3, 1fr); grid-template-rows: repeat(2, 1fr); }
  .photo { background: linear-gradient(180deg, #9aa4ab 0%, var(--photo) 100%); }
  .photo.alt { background: linear-gradient(180deg, #aab3b9 0%, #6f7a82 100%); }
  .top .band { position: absolute; left: 0; top: 374px; width: 750px; height: 21px; background: var(--slate); }
  .top .wordmark { position: absolute; left: 0; right: 0; top: 433px; text-align: center; color: var(--teal); font-size: 58px; }
  .top .tagline { position: absolute; left: 0; right: 0; top: 494px; text-align: center; color: var(--slate-dark); font-size: 20px; }

  /* back panel */
  .back { left: 226px; top: 1867px; width: 747px; height: 398px; background: var(--slate); }
  .back .pattern { position: absolute; inset: 0; background: linear-gradient(160deg, #c9d3da 0%, var(--slate) 60%, #b6c3cc 100%); }
  .back .wordmark { position: absolute; left: 0; right: 0; top: 142px; text-align: center; color: var(--white); font-size: 108px; letter-spacing: -4px; }
  .back .tagline { position: absolute; left: 114px; top: 243px; color: var(--white); font-size: 27px; }
  .back .rule { position: absolute; left: 114px; top: 286px; width: 555px; height: 4px; background: var(--teal); }

  /* features side */
  .features { left: 232px; top: 2298px; width: 660px; height: 479px; background: var(--white); }
  .features .title { position: absolute; left: 33px; top: 52px; font-size: 47px; color: var(--slate); white-space: nowrap; letter-spacing: -1px; }
  .features .title b { font-weight: 800; }
  .features .title span { font-weight: 600; }
  .feature { position: absolute; top: 136px; width: 175px; }
  .feature .icon-box { width: 175px; height: 173px; background: var(--slate); display: flex; align-items: center; justify-content: center; }
  .feature h3 { margin-top: 36px; font-size: 18px; font-weight: 700; color: var(--teal); white-space: nowrap; }
  .feature p { margin-top: 2px; font-size: 14.5px; font-weight: 600; line-height: 1.22; color: var(--ink); }

  /* info side */
  .info { left: 312px; top: 2811px; width: 660px; height: 479px; background: var(--white); }
  .info .wordmark { position: absolute; left: 72px; top: 108px; color: var(--slate); font-size: 80px; letter-spacing: -3px; }
  .info .rule { position: absolute; left: 80px; top: 203px; width: 580px; height: 5px; background: var(--teal); }
  .info ul { list-style: none; position: absolute; left: 76px; top: 251px; }
  .info li { display: flex; align-items: center; height: 57px; font-size: 24px; font-weight: 500; color: var(--ink); white-space: nowrap; }
  .info li b { font-weight: 700; margin-left: 7px; }
  .info li .dot { width: 18px; height: 18px; border-radius: 50%; border: 3px solid var(--teal); margin-right: 17px; flex: none; }
</style>
</head>
<body>

  <div class="brand-header wordmark">HERD SURE</div>

  <section class="panel front">
    <div class="pattern" role="img" aria-label="Fine wavy contour line pattern on teal"></div>
    <div class="wordmark">HERD SURE</div>
    <div class="tagline">Affordable Diagnostics for Healthy Herds</div>
  </section>

  <section class="panel top">
    <div class="photo-grid">
      <div class="photo" role="img" aria-label="Monochrome photo of a cow"></div>
      <div class="photo alt" role="img" aria-label="Monochrome photo of a pig"></div>
      <div class="photo" role="img" aria-label="Monochrome photo of a sheep in a field"></div>
      <div class="photo alt" role="img" aria-label="Monochrome photo of a hen"></div>
      <div class="photo" role="img" aria-label="Monochrome photo of a horse"></div>
      <div class="photo alt" role="img" aria-label="Monochrome photo of a white duck"></div>
    </div>
    <div class="band"></div>
    <div class="wordmark">HERD SURE</div>
    <div class="tagline">Affordable Diagnostics for Healthy Herds</div>
  </section>

  <section class="panel back">
    <div class="pattern" role="img" aria-label="Fine wavy contour line pattern on pale grey-blue"></div>
    <div class="wordmark">HERD SURE</div>
    <div class="tagline">Affordable Diagnostics for Healthy Herds</div>
    <div class="rule"></div>
  </section>

  <section class="panel features">
    <h2 class="title"><b>HERD SURE</b> <span>RAPID TEST</span></h2>

    <div class="feature" style="left:37px">
      <div class="icon-box">
        <svg width="130" height="130" viewBox="0 0 130 130" fill="none" stroke="#fff" stroke-width="2.5" stroke-linecap="round">
          <line x1="65" y1="8" x2="65" y2="24"/><line x1="65" y1="106" x2="65" y2="122"/>
          <line x1="8" y1="65" x2="24" y2="65"/><line x1="106" y1="65" x2="122" y2="65"/>
          <line x1="25" y1="25" x2="33" y2="33"/><line x1="105" y1="25" x2="97" y2="33"/>
          <line x1="25" y1="105" x2="33" y2="97"/><line x1="105" y1="105" x2="97" y2="97"/>
          <circle cx="65" cy="65" r="6"/>
          <line x1="65" y1="65" x2="65" y2="36"/><line x1="70" y1="63" x2="104" y2="50"/>
          <line x1="61" y1="69" x2="44" y2="84"/>
        </svg>
      </div>
      <h3>FAST &amp; EFFICIENT</h3>
      <p>Rapid test results in less than 10 minutes from preparation to completion.</p>
    </div>

    <div class="feature" style="left:243px">
      <div class="icon-box">
        <svg width="110" height="110" viewBox="0 0 110 110" fill="none" stroke="#fff" stroke-width="4" stroke-linejoin="round">
          <rect x="22" y="10" width="70" height="38" rx="3"/>
          <rect x="16" y="18" width="70" height="38" rx="3"/>
          <rect x="10" y="26" width="70" height="38" rx="3" fill="#bfcbd3"/>
          <circle cx="45" cy="45" r="8"/>
          <path d="M10 90 L30 74 Q38 68 48 72 L64 76 Q70 78 66 84 L52 84 L72 84 L96 68 Q104 64 100 74 L80 96 L36 98 L22 104 Z" fill="#fff"/>
        </svg>
      </div>
      <h3>AFFORDABLE</h3>
      <p>Colloidal gold-based rapid tests that combine high accuracy with cost-effectiveness.</p>
    </div>

    <div class="feature" style="left:447px">
      <div class="icon-box">
        <svg width="100" height="120" viewBox="0 0 100 120" fill="none" stroke="#fff" stroke-width="3">
          <path d="M50 6 L92 20 L92 58 Q92 94 50 114 Q8 94 8 58 L8 20 Z"/>
          <path d="M43 38 H57 V51 H70 V65 H57 V78 H43 V65 H30 V51 H43 Z" fill="#fff" stroke="none"/>
        </svg>
      </div>
      <h3>RELIABLE &amp; SIMPLE</h3>
      <p>Stable test performance with 2~30°C, easy to operate, no professional skills required.</p>
    </div>
  </section>

  <section class="panel info">
    <div class="wordmark">HERD SURE</div>
    <div class="rule"></div>
    <ul>
      <li><span class="dot"></span>Manufactured by<b>FIELDLINE BIO</b></li>
      <li><span class="dot"></span>Storage: 2-30°C,<b>Do not freeze!</b></li>
      <li><span class="dot"></span>See the instructions for other contents.</li>
    </ul>
  </section>

</body>
</html>
```